Design 4 pages for an event discovery website

This is a contest for the design of 4 pages for an events discovery website. The feature is part of the new sign-up process.

Please see the attached document for a full scope, mockups and the parent category icons.

Target Market(s)

18-35 Australian event goers

Industry/Entity Type

Events

Number of Pages Required

4 page

```html
<!DOCTYPE html>
<html lang="en">
<head>
<meta charset="utf-8">
<title>Ventora – Linking to other accounts</title>
<link rel="stylesheet" href="https://fonts.googleapis.com/css2?family=Oswald:wght@300;400&family=Roboto:wght@400&family=Varela+Round&display=swap">
<style>
  :root {
    --brand-blue: #2aa8e6;
    --text-grey: #444;
    --header-bg-top: #ffffff;
    --header-bg-bottom: #ececec;
    --signup: #1c9bdc;
    --login: #f58a2c;
    --panel: rgba(72, 150, 200, 0.78);
    --hero-dark: #0c1530;
    --hero-mid: #1d3c66;
    --hero-light: #5c8fb8;
    --chatter: #3a8fd6;
    --snap: #215f8c;
    --tune: #7cc424;
    --melodia: #5a70c2;
    --error-red: #e8332b;
    --white: #ffffff;
  }
  * { box-sizing: border-box; margin: 0; padding: 0; }
  html, body { width: 1200px; height: 837px; overflow: hidden; }
  body { position: relative; font-family: "Roboto", sans-serif; background: var(--white); }

  .site-header {
    position: absolute; left: 0; top: 0; width: 1200px; height: 115px;
    background: linear-gradient(var(--header-bg-top), var(--header-bg-bottom));
  }
  .brand {
    position: absolute; left: 88px; top: 40px;
    font-family: "Varela Round", sans-serif; font-size: 40px; line-height: 48px;
    color: var(--brand-blue); letter-spacing: 0;
  }
  .main-nav {
    position: absolute; left: 479px; top: 61px;
    font-size: 14px; color: var(--text-grey); letter-spacing: 0.3px;
  }
  .main-nav span.sep { margin: 0 10px; }
  .search {
    position: absolute; left: 621px; top: 46px; width: 236px; height: 45px;
    background: var(--white); border: 1px solid #cfcfcf;
  }
  .search span { position: absolute; left: 15px; top: 13px; font-size: 14px; color: #666; }
  .search svg { position: absolute; right: 13px; top: 12px; }
  .btn {
    position: absolute; top: 47px; width: 114px; height: 42px;
    color: var(--white); font-size: 16px; text-align: center; line-height: 42px; border-radius: 2px;
  }
  .btn-signup { left: 877px; background: var(--signup); }
  .btn-login { left: 999px; top: 48px; background: var(--login); }

  .hero {
    position: absolute; left: 0; top: 115px; width: 1200px; height: 607px;
    background:
      radial-gradient(ellipse at 55% 25%, rgba(110,160,200,0.55), transparent 60%),
      radial-gradient(ellipse at 85% 50%, rgba(120,120,140,0.35), transparent 50%),
      linear-gradient(180deg, var(--hero-mid) 0%, var(--hero-dark) 85%);
  }
  .intro-panel {
    position: absolute; left: 87px; top: 115px; width: 1026px; height: 199px;
    background: var(--panel); color: var(--white); text-align: center;
    font-family: "Oswald", sans-serif;
  }
  .intro-panel h1 { font-weight: 400; font-size: 38px; margin-top: 30px; letter-spacing: -0.5px; }
  .intro-panel p { font-weight: 300; font-size: 23px; line-height: 34px; margin-top: 12px; letter-spacing: -0.3px; }

  .account {
    position: absolute; left: 89px; width: 204px; height: 56px;
    color: var(--white); font-family: "Varela Round", sans-serif; font-size: 22px;
    display: flex; align-items: center; border-radius: 2px;
  }
  .account .icon {
    width: 63px; height: 100%; display: flex; align-items: center; justify-content: center;
    background: rgba(0,0,0,0.1);
  }
  .account .icon i { width: 24px; height: 24px; border-radius: 5px; background: var(--white); display: block; }
  .account .label { padding-left: 18px; }
  .account-chatter { top: 378px; background: var(--chatter); }
  .account-snap { top: 447px; background: var(--snap); }
  .account-tune { top: 515px; background: var(--tune); }
  .account-melodia { top: 584px; background: var(--melodia); }

  .status {
    position: absolute; left: 307px; display: flex; align-items: center; gap: 12px;
    font-family: "Oswald", sans-serif; font-size: 20px; color: var(--white);
  }
  .status-linked { top: 392px; }
  .status-missing { top: 532px; }

  .site-footer {
    position: absolute; left: 0; top: 722px; width: 1200px; height: 115px;
    background: linear-gradient(var(--header-bg-top), var(--header-bg-bottom));
    color: var(--text-grey);
  }
  .footer-links { position: absolute; left: 90px; top: 34px; font-size: 13px; }
  .footer-links span.sep { margin: 0 6px; }
  .copyright { position: absolute; left: 90px; top: 61px; font-size: 15px; }
  .social { position: absolute; left: 953px; top: 45px; display: flex; gap: 12px; }
  .social i { width: 33px; height: 33px; background: var(--signup); display: block; border-radius: 2px; }
</style>
</head>
<body>
  <header class="site-header">
    <div class="brand">VENTORA</div>
    <nav class="main-nav">FIND<span class="sep">|</span>EVENTS</nav>
    <div class="search">
      <span>Search</span>
      <svg width="20" height="20" viewBox="0 0 20 20" aria-hidden="true">
        <circle cx="8" cy="8" r="6" fill="none" stroke="#111" stroke-width="2"/>
        <line x1="12.5" y1="12.5" x2="18" y2="18" stroke="#111" stroke-width="3" stroke-linecap="round"/>
      </svg>
    </div>
    <div class="btn btn-signup">SIGN UP</div>
    <div class="btn btn-login">LOGIN</div>
  </header>

  <div class="hero" role="img" aria-label="Concert crowd with raised hands under blue stage lights"></div>

  <section class="intro-panel">
    <h1>LINKING TO OTHER ACCOUNTS</h1>
    <p>Link in all your other Social media acount and music players<br>by linking your account, wecan save you a lot time by automatically your intersts</p>
  </section>

  <div class="account account-chatter"><div class="icon"><i></i></div><span class="label">Chatterly</span></div>
  <div class="account account-snap"><div class="icon"><i></i></div><span class="label">Snapframe</span></div>
  <div class="account account-tune"><div class="icon"><i style="border-radius:50%"></i></div><span class="label">Tunewave</span></div>
  <div class="account account-melodia"><div class="icon"><i style="border-radius:50%"></i></div><span class="label">Melodia</span></div>

  <div class="status status-linked">
    <svg width="23" height="23" viewBox="0 0 23 23" aria-hidden="true">
      <rect width="23" height="23" rx="3" fill="#fff"/>
      <path d="M5 12 L10 17 L18 6" fill="none" stroke="#1d3c66" stroke-width="3"/>
    </svg>
    <span>LINKED</span>
  </div>
  <div class="status status-missing">
    <svg width="18" height="18" viewBox="0 0 18 18" aria-hidden="true">
      <path d="M2 2 L16 16 M16 2 L2 16" stroke="var(--error-red)" stroke-width="4" stroke-linecap="round"/>
    </svg>
    <span>WE DON'T HAVE THAT YET BUT HAVE RECARDED YOUR INTEREST</span>
  </div>

  <footer class="site-footer">
    <div class="footer-links">About<span class="sep">|</span>Disclaimer<span class="sep">|</span>Contact<span class="sep">|</span>Sitemap<span class="sep">|</span>Hosted Solutions Partner</div>
    <div class="copyright">Copyright © 2015&nbsp; All Rights</div>
    <div class="social"><i></i><i></i><i></i><i></i></div>
  </footer>
</body>
</html>
```